Business Cards

Now that we have a fantastic logo, we need business cards designed for our organization.
We'd like a design that uses our logo and is very creative and eye catching. It should have the following copy, in addition to our logo. It can be standard business card size, or smaller.
Cultivate. Connect. Create.
418 Ember Lane
Alderbrook, California
Hollis County
California
United States of America
url: www.emberlaneguild.org
chirper: #embercraft
facepage, linkwork, searchnet+, and tumblepost: ember lane guild
email: info@emberlaneguild

```html
<!DOCTYPE html>
<html lang="en">
<head>
<meta charset="utf-8">
<title>Ember Lane Guild – Business Card Proposal</title>
<link rel="stylesheet" href="https://fonts.googleapis.com/css2?family=Arvo&family=Lato&display=swap">
<style>
  :root {
    --sheet: #e7e8ea;
    --card: #bcbdbf;
    --ember: #ec7f2b;
    --ink: #3f3f40;
    --ink-dark: #1e1e1e;
    --white: #ffffff;
  }
  html, body {
    margin: 0;
    padding: 0;
    width: 1200px;
    height: 986px;
    overflow: hidden;
    background: var(--sheet);
  }
  .sheet {
    position: relative;
    width: 1200px;
    height: 986px;
    background: var(--sheet);
  }
  .card {
    position: absolute;
    left: 383px;
    top: 102px;
    width: 460px;
    height: 766px;
    background: var(--card);
  }
  .brand {
    position: absolute;
    left: 0;
    top: 43px;
    width: 460px;
    height: 290px;
    display: flex;
    flex-direction: column;
    align-items: center;
    justify-content: flex-end;
    gap: 36px;
  }
  .brand-mark {
    width: 140px;
    height: 140px;
    background: var(--ember);
  }
  .brand-name {
    margin: 0;
    font-family: "Arvo", serif;
    font-size: 28px;
    line-height: 32px;
    font-weight: 400;
    color: var(--ink);
    letter-spacing: -0.5px;
  }
  .address-band {
    position: absolute;
    left: 0;
    top: 373px;
    width: 460px;
    height: 147px;
    background: var(--ember);
    display: flex;
    align-items: center;
    justify-content: center;
  }
  .address {
    margin: 0;
    font-family: "Arvo", serif;
    font-style: normal;
    font-size: 23px;
    line-height: 33px;
    color: var(--white);
    text-align: center;
  }
  .contacts {
    position: absolute;
    left: 0;
    top: 556px;
    width: 460px;
    margin: 0;
    font-family: "Arvo", serif;
    font-size: 21px;
    line-height: 32.5px;
    letter-spacing: -0.6px;
    color: var(--ink);
    text-align: center;
  }
  .proposal-note {
    position: absolute;
    left: 30px;
    top: 910px;
    margin: 0;
    font-family: "Lato", sans-serif;
    font-size: 28px;
    letter-spacing: 1.4px;
    color: var(--ink-dark);
    white-space: nowrap;
  }
</style>
</head>
<body>
<main class="sheet">
  <section class="card" aria-label="Business card">
    <div class="brand">
      <div class="brand-mark"></div>
      <p class="brand-name">ember lane guild</p>
    </div>
    <div class="address-band">
      <address class="address">
        418 Ember Lane<br>
        Alderbrook, California<br>
        Hollis County California<br>
        United States of America
      </address>
    </div>
    <p class="contacts">
      url: www.emberlaneguild.org<br>
      chirper: #embercraft<br>
      facepage, linkwork, searchnet+<br>
      and tumblepost: ember lane guild<br>
      email: info@emberlaneguild
    </p>
  </section>
  <p class="proposal-note">This design is presented as proposal and can be edited upon request.</p>
</main>
</body>
</html>
```